Halvorn Pin Keeper Brochure

We need a brochure to promote a brand new patented product. The product is a lock that ensure a shipping container itself cannot be stolen as even though you can stop someone breaking into a shipping container up until now you could not stop them from simply stealing the entire container using a crane/hyab truck/tilt tray truck/etc. This product is therefore all about security of the high value items with the container. The lock works in conjunction with standard shipping container 'twist locks'.
We would like our logo within the design. We can supply more images of required as this product is 3D modeled so you need only ask.

```html
<!DOCTYPE html>
<html lang="en">
<head>
<meta charset="utf-8">
<title>Halvorn Pin Keeper Brochure</title>
<link rel="stylesheet" href="https://fonts.googleapis.com/css2?family=Open+Sans:wght@400;600;700&display=swap">
<style>
:root{
  --stage:#3a1519;
  --red:#c8231f;
  --red-deep:#8e1412;
  --ink:#5a5a5a;
  --wine:#7a1210;
  --paper:#ffffff;
  --brand-grey:#6b6b6b;
}
*{box-sizing:border-box;margin:0;padding:0}
html,body{width:1200px;height:848px;overflow:hidden;background:var(--stage)}
body{font-family:"Open Sans",Arial,sans-serif;position:relative}
.page{position:absolute;top:64px;width:520px;height:720px;background:var(--paper);overflow:hidden;box-shadow:0 6px 24px rgba(0,0,0,.45)}
.page--cover{left:60px}
.page--inside{left:620px}
.page svg.shapes{position:absolute;inset:0}
.photo{position:absolute}
.cover-title{position:absolute;left:150px;top:478px;color:#fff;font-weight:700;font-size:22px;line-height:28px;letter-spacing:.3px}
.brand{position:absolute;left:150px;top:628px;display:flex;align-items:center;gap:12px}
.brand__mark{width:20px;height:20px;background:var(--red)}
.brand__name{color:var(--brand-grey);font-weight:600;font-size:28px;line-height:32px}
.quote{position:absolute;left:338px;top:104px;width:168px;text-align:center;color:var(--wine);font-weight:700;font-size:14.5px;line-height:18.5px}
.section-title{position:absolute;left:40px;top:318px;color:#fff;font-weight:700;font-size:17px;letter-spacing:.3px}
.columns{position:absolute;left:38px;top:402px;width:448px;column-count:2;column-gap:22px;font-size:9.6px;line-height:13.2px;color:var(--ink);text-align:justify}
.columns p{text-indent:12px;margin-bottom:13px}
.columns h3{color:var(--red);font-weight:400;font-size:14.5px;line-height:16px;margin:4px 0 2px}
.columns strong{color:var(--red-deep)}
</style>
</head>
<body>

<section class="page page--cover">
  <svg class="shapes" width="520" height="720" viewBox="0 0 520 720">
    <defs>
      <linearGradient id="coverRed" x1="0" y1="0" x2="1" y2="1">
        <stop offset="0" stop-color="#9a1613"/>
        <stop offset=".5" stop-color="#cf2a22"/>
        <stop offset="1" stop-color="#e04532"/>
      </linearGradient>
    </defs>
    <path d="M0 0H520V470Q400 580 0 590Z" fill="url(#coverRed)"/>
    <path d="M0 560Q350 560 520 455V540Q400 600 0 610Z" fill="#7d1210" opacity=".35"/>
  </svg>
  <div class="photo" role="img" aria-label="Container corner casting with the lock fitted"
       style="left:40px;top:40px;width:226px;height:210px;background:linear-gradient(135deg,#a54a48,#c7807a 55%,#efe0b4)"></div>
  <div class="photo" role="img" aria-label="Close-up render of the red lock inside a grey corner fitting"
       style="left:270px;top:40px;width:250px;height:210px;border-top-left-radius:110px 90px;background:radial-gradient(circle at 40% 45%,#7b7b7b,#a9a9a9 45%,#9fc6ea 80%)"></div>
  <div class="photo" role="img" aria-label="Stacked red container corners with the lock in place"
       style="left:40px;top:254px;width:226px;height:210px;background:linear-gradient(160deg,#b45754,#8f3633 60%,#d9d9d9)"></div>
  <div class="photo" role="img" aria-label="Stacks of shipping containers under a sunny sky"
       style="left:270px;top:254px;width:250px;height:210px;background:linear-gradient(180deg,#4f8fd6,#cfe4f7 50%,#9a5650 75%,#3f6a9a)"></div>
  <h1 class="cover-title">SHIPPING CONTAINER<br>TWIST LOCKS</h1>
  <div class="brand"><span class="brand__mark"></span><span class="brand__name">Tarnwick Works</span></div>
</section>

<section class="page page--inside">
  <svg class="shapes" width="520" height="720" viewBox="0 0 520 720">
    <defs>
      <linearGradient id="insideRed" x1="0" y1="0" x2="1" y2="1">
        <stop offset="0" stop-color="#8e1412"/>
        <stop offset=".6" stop-color="#c8231f"/>
        <stop offset="1" stop-color="#e24a36"/>
      </linearGradient>
    </defs>
    <path d="M0 0H290Q430 40 430 190Q430 330 300 350H0Z" fill="url(#insideRed)"/>
    <path d="M0 300H290Q340 300 370 280Q350 340 290 350H0Z" fill="#7d1210" opacity=".45"/>
  </svg>
  <div class="photo" role="img" aria-label="3D render of the grey lock with its long rod"
       style="left:30px;top:30px;width:270px;height:262px;border-radius:0 130px 130px 0;background:radial-gradient(circle at 35% 45%,#6f6f6f,#9a9a9a 35%,#f3e7c0 70%)"></div>
  <p class="quote">“Our shipping container locks ensure your container is safe from theft by any means. It ensures your container cannot be removed from it’s footings by anyone but the owner”.</p>
  <h2 class="section-title">ABOUT THE PRODUCT</h2>
  <div class="columns">
    <p>Your shipping container can be easily locked securely shut, but what is stopping someone from simply picking up the entire container and stealing it with all your belongings inside? We have developed a patented locking system that allows you to easily lock your shipping container to footings or to another shipping container if you are multiple stacking.</p>
    <p>Our shipping container locks ensure your container is safe from theft by any means. It ensures your container cannot be removed from it’s footings by anyone but the owner. If you need security in a shipping container yard simple use the lock to connect and lock two shipping containers together vertically. It is impossible for double stacked shipping containers to be transported due to their height even if they can be picked up!</p>
    <p>The lock is easily installed and removed in a matter of seconds, they are available individually keyed or keyed alike and are manufactured in Stainless Steel.</p>
    <h3>How does it work?</h3>
    <p>Our patented design works in conjunction with a standard double ended, weldable or boltable twist lock in a way that ensures the twist lock cannot be opened once the lock is installed.</p>
    <p>A minimum of two Halvorn Pin Keepers are needed per container, located in opposite corners but we advise for maximum security four should be used, one in each corner.</p>
    <p>So, the answer as to how do you stop someone stealing your shipping container is now easily answered, simply install our <strong>Halvorn Pin Keeper.</strong></p>
  </div>
</section>

</body>
</html>
```